Clean professional design needed for landscape property business

We need a logo for a new lawncare, landscaping , property maintenance business called Meadow Trim.
Our services include lawn mowing, garden maintenance, clean ups and some property maintenance.
We want a double sided business card that is clean and very professional using the colour scheme from our logo which is provided.
the business card should have impact as we will use these to drop into people's letterboxes as a marketing drop.
Initially we want to see what you come up with so there is a very wide scope here to work with.
Updates

Project Deadline Extended
Reason: we feel our original deadline was too short. we have extended to give more time for quality submissions.

Target Market(s)

High end property owners who don't wish to do there own gardneing or property maintenance

Industry/Entity Type

Business

Contact Information for Business Card

Name
Postion/ Title
Phone number
mobile
web address
physical address

services offered

Font styles to use
Sans Serif

Requirements
Must have
• curved edges preferrred
Nice to have
• We like the idea of the logo being embossed or etched into the card so it looks like it is below the surface of the card
Should not have
• No stock images or characters.

```html
<!DOCTYPE html>
<html lang="en">
<head>
<meta charset="utf-8">
<title>Meadow Trim – Business Card</title>
<link href="https://fonts.googleapis.com/css2?family=Open+Sans:wght@400;600;700&display=swap" rel="stylesheet">
<style>
  :root {
    --backdrop: #3a332f;
    --card: #121212;
    --card-edge: #1c1c1c;
    --green: #7dc21e;
    --text: #e8e8e8;
    --muted: #b5b5b5;
  }
  * { box-sizing: border-box; margin: 0; padding: 0; }
  html, body { width: 1200px; height: 844px; overflow: hidden; }
  body {
    background: var(--backdrop);
    font-family: "Open Sans", Arial, sans-serif;
    display: flex;
    align-items: center;
    justify-content: center;
    gap: 60px;
  }
  .card {
    position: relative;
    width: 520px;
    height: 300px;
    background: var(--card);
    border: 1px solid var(--card-edge);
    border-radius: 16px;
    box-shadow: 0 18px 40px rgba(0,0,0,.45);
    overflow: hidden;
  }
  .wordmark {
    display: flex;
    align-items: center;
    gap: 10px;
    font-weight: 700;
    color: var(--green);
    letter-spacing: -1.5px;
  }
  .wordmark .mark {
    width: 22px; height: 22px;
    background: var(--green);
  }
  /* front */
  .card--front .wordmark {
    position: absolute; left: 60px; top: 58px;
    font-size: 48px;
  }
  .holder {
    position: absolute; left: 60px; top: 150px;
  }
  .holder__name { color: var(--green); font-weight: 600; font-size: 19px; }
  .holder__role { color: var(--muted); font-size: 14px; margin-top: 2px; }
  .contacts {
    position: absolute; left: 270px; top: 140px;
    list-style: none;
    color: var(--text); font-size: 14px;
  }
  .contacts li { display: flex; align-items: center; gap: 10px; line-height: 22px; }
  .contacts svg { width: 12px; height: 12px; fill: var(--green); flex: none; }
  .divider {
    position: absolute; left: 0; right: 0; top: 222px;
    height: 1.5px; background: var(--green);
  }
  .address {
    position: absolute; left: 60px; top: 238px;
    color: var(--text); font-size: 15px;
  }
  /* back */
  .card--back .wordmark {
    position: absolute; left: 80px; top: 60px;
    font-size: 44px;
  }
  .services {
    position: absolute; left: 250px; top: 140px;
  }
  .services__title {
    color: var(--green); font-weight: 600; font-size: 13px;
    letter-spacing: .5px; margin-bottom: 6px;
  }
  .services ul { list-style: none; color: var(--text); font-size: 14px; }
  .services li { display: flex; align-items: center; gap: 9px; line-height: 21px; }
  .services li::before {
    content: ""; width: 7px; height: 7px; background: var(--green); flex: none;
  }
</style>
</head>
<body>
  <section class="card card--front" aria-label="Business card front">
    <div class="wordmark"><span>meadowtrim</span><span class="mark"></span></div>
    <div class="holder">
      <p class="holder__name">Daniel Hart</p>
      <p class="holder__role">Project Manager</p>
    </div>
    <ul class="contacts">
      <li><svg viewBox="0 0 24 24"><path d="M6.6 10.8a15.1 15.1 0 0 0 6.6 6.6l2.2-2.2a1 1 0 0 1 1-.25 11.4 11.4 0 0 0 3.6.57 1 1 0 0 1 1 1V20a1 1 0 0 1-1 1A17 17 0 0 1 3 4a1 1 0 0 1 1-1h3.5a1 1 0 0 1 1 1c0 1.25.2 2.45.57 3.57a1 1 0 0 1-.25 1z"/></svg>555 014 2290</li>
      <li><svg viewBox="0 0 24 24"><path d="M2 5h20v14H2zM3.5 6.5 12 12.5l8.5-6z"/></svg>hello@meadowtrim.com</li>
      <li><svg viewBox="0 0 24 24"><circle cx="12" cy="12" r="10"/></svg>www.meadowtrim.com</li>
    </ul>
    <div class="divider"></div>
    <p class="address">Address Line1, Address Line2, country -123456</p>
  </section>

  <section class="card card--back" aria-label="Business card back">
    <div class="wordmark"><span>meadowtrim</span><span class="mark"></span></div>
    <div class="services">
      <p class="services__title">SERVICES OFFERED</p>
      <ul>
        <li>Lawn mowing</li>
        <li>Garden maintenance</li>
        <li>Clean ups</li>
        <li>Property maintenance</li>
      </ul>
    </div>
  </section>
</body>
</html>
```